Web Page Color Scheme

I need the colors chosen for all of the elements in a B2B web application page (screenshot attached).

We have a web application that serves businesses (not consumers), generally Corvane 300 companies. The pages are fully developed/functional. What I want is to improve the look and feel so that the page has a more premium feel. That is the entire goal, to make the pages have a very premium feel to them. I don’t know if it is the best analogy but if you think of Varn or Pallisene as average and KTR or Osprin as premium, we want users to get a very premium feel the first time they see the screens.

What I am looking for right now is just colors. Below I describe the details.

#1 Improve the colors

The color scheme is blue and yellow. Black, gray and white are also used. I do not think the base colors should change (that is, I think we will continue to use blue and yellow) but I do think which hues, shades, tints or tones of blue, yellow and gray we use could benefit from some improvement. Feel free to use any blues, yellows and grays you think look best, lighter or darker colors, etc. You can also feel free to change what colors are used where. One note, aqua blue does not look premium. It might be deco looking or otherwise good for some things but I don’t think you will see an aqua colored Hollaway driving down the street any time soon.

Quill products tend to have a premium feel but I don’t think I am looking for a stark white appearance.

I want every color defined including but not necessarily limited to:

Backgrounds

Page Header
Navigation Panel
Page Body
Table Header
Table Header Button (the Add button)
Table Column Header
Table Rows (maybe alternating, maybe not)
Checkboxes
Table Footer

Not all of these have to be different. I assume some will be the same. I just need each carefully
thought through.

Fonts

Page Header
Navigation Panel
Page Title
Table Header Title
Table Header Button
Table Column Header
Table Row
Table Footer

Icons

Page Header
Navigation Panel
Table expander/collapse
Actions
Table Footer

Target Market(s)

Corvane 300/Pinnacle 1200

Requirements
Must have
• Premium feel

```html
<!DOCTYPE html>
<html lang="en">
<head>
<meta charset="utf-8">
<title>Acme Data – Data Sources</title>
<link href="https://fonts.googleapis.com/css2?family=Roboto:wght@400;500;700&display=swap" rel="stylesheet">
<style>
:root{
  --navy:#1f2d86;
  --navy-dark:#18236e;
  --gold:#f4c542;
  --white:#ffffff;
  --text:#555a63;
  --text-head:#1f2d86;
  --line:#dcdde2;
  --row-alt:#f5f5f7;
  --muted:#b9bcc4;
}
*{box-sizing:border-box;margin:0;padding:0}
html,body{width:1200px;height:1067px;overflow:hidden;background:var(--white);font-family:"Roboto",Arial,sans-serif}
.app{position:relative;width:1200px;height:1067px}
.topbar{position:absolute;left:0;top:0;width:1200px;height:72px;background:var(--navy);color:var(--white);display:flex;align-items:center}
.brand{display:flex;align-items:center;margin-left:30px;font-size:27px;font-weight:400;letter-spacing:.2px}
.brand-mark{width:20px;height:20px;border-radius:50%;background:var(--gold);margin-right:38px}
.menu-toggle{margin-left:50px}
.top-tools{margin-left:auto;display:flex;align-items:center;gap:14px;margin-right:10px}
.user{font-size:13px;display:flex;align-items:center;gap:8px;margin-left:16px}
.sidebar{position:absolute;left:0;top:72px;width:247px;height:963px;background:var(--navy);color:var(--white)}
.nav-item{position:absolute;display:flex;align-items:center;gap:10px;font-size:13px;font-weight:500}
.nav-item.active{color:var(--gold)}
.nav-item svg{width:17px;height:17px}
.main{position:absolute;left:262px;top:72px;width:938px}
.page-title{position:absolute;left:0;top:14px;font-size:26px;color:var(--navy);font-weight:400}
.search{position:absolute;left:690px;top:15px;width:246px;height:27px;border:1px solid #c9cbd1;display:flex}
.search span{margin-left:auto;width:32px;border-left:1px solid #c9cbd1;background:#f0f0f2;display:flex;align-items:center;justify-content:center}
.panel{position:absolute;top:58px;left:0;width:938px;border-left:1px solid var(--line)}
.band{height:33px;background:var(--navy);color:var(--white);display:flex;align-items:center;padding-left:9px;font-size:16px;font-weight:500}
.add-btn{margin-left:14px;border:1px solid var(--white);color:var(--gold);font-size:14px;padding:0 6px;line-height:17px;font-weight:400}
.band.sub .add-btn{color:var(--white)}
.row{display:grid;align-items:center;height:28px;border-bottom:1px solid var(--line);font-size:13px;color:var(--text)}
.row.alt{background:var(--row-alt)}
.col-head{height:29px;color:var(--text-head);font-size:14px;border-bottom:1px solid var(--line)}
.ds{grid-template-columns:21px 255px 257px 260px 1fr}
.ds .acts{display:flex;gap:13px;justify-content:flex-end;padding-right:22px}
.ds.col-head .acts{padding-right:34px}
.ds.split>div{border-right:1px solid var(--line);height:100%;display:flex;align-items:center}
.ds.split>div:first-child{border:none}
.exp{display:flex;justify-content:center}
.nest1{margin-left:20px;border-left:1px solid var(--line)}
.nest2{margin-left:20px;border-left:1px solid var(--line)}
.dobj{grid-template-columns:22px 1fr 90px 66px;height:29px}
.dobj .count{text-align:right;padding-right:16px;border-right:1px solid var(--line);height:100%;display:flex;align-items:center;justify-content:flex-end}
.dobj .del{display:flex;justify-content:center}
.dobj.col-head{grid-template-columns:26px 1fr 66px}
.fld{grid-template-columns:255px 255px 100px 210px 1fr}
.fld>div{padding-left:7px;height:100%;display:flex;align-items:center;border-right:1px solid var(--line)}
.fld>div:last-child{border-right:none}
.fld.col-head>div{border:none}
.fld .pk{justify-content:center;padding:0}
.fld.col-head .pk{justify-content:flex-start;padding-left:15px}
.box{width:15px;height:15px;border:1px solid #d6d7dc;border-radius:2px;background:#fff}
.box.on{background:#c9cacf;border-color:#c9cacf;display:flex;align-items:center;justify-content:center}
.rules{gap:14px;padding-left:14px!important}
.fld.col-head .rules{padding-left:67px!important}
.rules.off{opacity:.35}
.fld .acts{gap:16px;padding-left:9px!important}
.fade{opacity:.45}
.pager{height:30px;display:flex;align-items:center;font-size:13px;color:var(--text);padding-left:16px;border-bottom:1px solid var(--line);border-right:1px solid var(--line)}
.pager select{margin-left:6px;width:50px;height:19px;font-size:12px;color:var(--text);border:1px solid #c9cbd1;background:#fff}
.pages{margin-left:245px;display:flex;gap:18px;align-items:center}
.footer{position:absolute;left:0;top:1035px;width:1200px;height:32px;background:var(--navy);color:var(--white);font-size:12px;display:flex;align-items:center;justify-content:center;padding-left:40px}
.ic{width:15px;height:15px;color:var(--navy)}
</style>
</head>
<body>
<svg width="0" height="0" style="position:absolute">
  <defs>
    <symbol id="bolt" viewBox="0 0 16 16"><path d="M9 1 4 9h4l-1 6 5-8H8z" fill="currentColor"/></symbol>
    <symbol id="edit" viewBox="0 0 16 16"><rect x="1.5" y="3.5" width="11" height="11" fill="none" stroke="currentColor" stroke-width="1.6"/><path d="M6 10l1-3 7-6 2 2-7 6z" fill="currentColor"/></symbol>
    <symbol id="copy" viewBox="0 0 16 16"><rect x="1.5" y="4.5" width="9" height="10" fill="none" stroke="currentColor" stroke-width="1.6"/><rect x="5.5" y="1.5" width="9" height="10" fill="#fff" stroke="currentColor" stroke-width="1.6"/></symbol>
    <symbol id="trash" viewBox="0 0 16 16"><path d="M2 3h12v2H2zM6 1h4v2H6zM3.5 6h9l-1 9h-7z" fill="currentColor"/><path d="M6.5 8v5M9.5 8v5" stroke="#fff" stroke-width="1"/></symbol>
    <symbol id="chev-r" viewBox="0 0 16 16"><path d="M5 3l6 5-6 5" fill="none" stroke="currentColor" stroke-width="2.4"/></symbol>
    <symbol id="chev-d" viewBox="0 0 16 16"><path d="M3 5l5 6 5-6" fill="none" stroke="currentColor" stroke-width="2.4"/></symbol>
    <symbol id="r-text" viewBox="0 0 16 16"><text x="0" y="14" font-size="13" font-family="Roboto,Arial,sans-serif" font-weight="700" fill="currentColor">a</text><path d="M9 6l2 2 4-6" fill="none" stroke="currentColor" stroke-width="1.6"/></symbol>
    <symbol id="r-find" viewBox="0 0 16 16"><circle cx="9" cy="6" r="4.2" fill="none" stroke="currentColor" stroke-width="2"/><path d="M6 9l-5 5" stroke="currentColor" stroke-width="2.6"/></symbol>
    <symbol id="r-dup" viewBox="0 0 16 16"><rect x=".7" y=".7" width="14.6" height="14.6" fill="none" stroke="currentColor" stroke-width="1.2"/><rect x="3" y="6" width="7" height="7" fill="none" stroke="currentColor" stroke-width="1.5"/><rect x="6" y="3" width="7" height="7" fill="#fff" stroke="currentColor" stroke-width="1.5"/></symbol>
    <symbol id="r-branch" viewBox="0 0 16 16"><circle cx="3" cy="3" r="2" fill="currentColor"/><circle cx="13" cy="3" r="2" fill="currentColor"/><circle cx="8" cy="14" r="2" fill="currentColor"/><path d="M3 3v3l5 4v4M13 3v3l-5 4" fill="none" stroke="currentColor" stroke-width="1.4"/></symbol>
    <symbol id="r-globe" viewBox="0 0 16 16"><circle cx="8" cy="8" r="6.5" fill="none" stroke="currentColor" stroke-width="1.5"/><circle cx="8" cy="8" r="2.5" fill="currentColor"/><path d="M8 0v4M8 12v4M0 8h4M12 8h4" stroke="currentColor" stroke-width="1.5"/></symbol>
    <symbol id="r-list" viewBox="0 0 16 16"><rect x="1" y="2" width="14" height="2" fill="currentColor"/><rect x="1" y="6" width="14" height="4" fill="currentColor"/><rect x="1" y="12" width="14" height="2" fill="currentColor"/></symbol>
  </defs>
</svg>

<div class="app">
  <header class="topbar">
    <div class="brand"><span class="brand-mark"></span>Acme Data</div>
    <svg class="menu-toggle" width="16" height="14" viewBox="0 0 16 14"><path d="M1 2h14M1 7h14M1 12h14" stroke="#fff" stroke-width="2"/></svg>
    <div class="top-tools">
      <svg width="22" height="16" viewBox="0 0 22 16"><path d="M2 14a9 9 0 0 1 18 0" fill="none" stroke="#fff" stroke-width="1.6"/><path d="M11 14l4-7" stroke="#fff" stroke-width="1.6"/></svg>
      <svg width="22" height="20" viewBox="0 0 22 20"><path d="M2 19 14 7" stroke="#fff" stroke-width="2.4"/><path d="M16 1v4M14 3h4M19 8v3M17.5 9.5h3M10 2v2M9 3h2" stroke="#fff" stroke-width="1.4"/></svg>
      <svg width="21" height="21" viewBox="0 0 21 21"><circle cx="10.5" cy="10.5" r="10" fill="#fff"/><text x="10.5" y="16" text-anchor="middle" font-size="14" font-weight="700" font-family="Roboto,Arial,sans-serif" fill="#1f2d86">?</text></svg>
      <svg width="21" height="21" viewBox="0 0 21 21"><circle cx="10.5" cy="10.5" r="6.5" fill="none" stroke="#fff" stroke-width="5" stroke-dasharray="3.4 1.7"/><circle cx="10.5" cy="10.5" r="5" fill="#fff"/><circle cx="10.5" cy="10.5" r="2.4" fill="#1f2d86"/></svg>
      <div class="user">Dale Marrow <svg width="10" height="6" viewBox="0 0 10 6"><path d="M0 0h10L5 6z" fill="#fff"/></svg></div>
    </div>
  </header>

  <nav class="sidebar">
    <div class="nav-item" style="left:18px;top:24px"><svg viewBox="0 0 18 16"><circle cx="6" cy="5" r="3.2" fill="#fff"/><circle cx="13" cy="5" r="2.6" fill="#fff"/><path d="M0 15c0-5 12-5 12 0zM12 10c3-1 6 0 6 5h-5z" fill="#fff"/></svg>Users</div>
    <div class="nav-item" style="left:67px;top:60px">Roles</div>
    <div class="nav-item" style="left:67px;top:95px">Notification Groups</div>
    <div class="nav-item active" style="left:18px;top:130px"><svg viewBox="0 0 16 16"><ellipse cx="8" cy="3" rx="6" ry="2.5" fill="#f4c542"/><path d="M2 5c0 3 12 3 12 0v3c0 3-12 3-12 0zM2 10c0 3 12 3 12 0v3c0 3-12 3-12 0z" fill="#f4c542"/></svg>Data Sources</div>
    <div class="nav-item" style="left:34px;top:166px"><svg viewBox="0 0 17 17"><rect x="1" y="6" width="5" height="5" fill="none" stroke="#fff" stroke-width="1.4"/><rect x="11" y="1" width="5" height="5" fill="none" stroke="#fff" stroke-width="1.4"/><rect x="11" y="11" width="5" height="5" fill="none" stroke="#fff" stroke-width="1.4"/><path d="M6 8.5h3V3.5h2M9 8.5v5h2" fill="none" stroke="#fff" stroke-width="1.4"/></svg>Data Object Relationships</div>
    <div class="nav-item" style="left:18px;top:202px"><svg viewBox="0 0 17 17"><g fill="none" stroke="#fff" stroke-width="1.4"><rect x="1" y="1" width="6" height="4"/><rect x="10" y="1" width="6" height="4"/><rect x="1" y="7" width="6" height="4"/><rect x="10" y="7" width="6" height="4"/><rect x="1" y="13" width="6" height="3"/><rect x="10" y="13" width="6" height="3"/></g></svg>Data Sets</div>
    <div class="nav-item" style="left:18px;top:238px"><svg viewBox="0 0 17 17"><path d="M1 2h3M1 7h3M1 12h3M6 2h10M6 7h10M6 12h10M8 16h8" stroke="#fff" stroke-width="2"/></svg>Rule Sets</div>
    <div class="nav-item" style="left:18px;top:274px"><svg viewBox="0 0 17 17"><circle cx="8.5" cy="8.5" r="7" fill="none" stroke="#fff" stroke-width="1.6"/><path d="M8.5 4v5h3" fill="none" stroke="#fff" stroke-width="1.6"/></svg>Schedules</div>
    <div class="nav-item" style="left:18px;top:310px"><svg viewBox="0 0 18 16"><path d="M2 6h10l-3-4M16 10H6l3 4" fill="none" stroke="#fff" stroke-width="2.6"/></svg>Metadata Import/Export</div>
    <div class="nav-item" style="left:67px;top:346px">Import</div>
    <div class="nav-item" style="left:67px;top:381px">Export</div>
  </nav>

  <main class="main">
    <h1 class="page-title">Data Sources</h1>
    <div class="search"><span><svg width="12" height="12" viewBox="0 0 12 12"><circle cx="5" cy="5" r="3.8" fill="none" stroke="#555" stroke-width="1.6"/><path d="M8 8l3.5 3.5" stroke="#555" stroke-width="1.8"/></svg></span></div>

    <section class="panel">
      <div class="band">Data Sources <span class="add-btn">Add</span></div>
      <div class="row ds col-head"><div></div><div>Data Source Name</div><div>Type</div><div>Status</div><div class="acts">Actions</div></div>
      <div class="row ds"><div class="exp"><svg class="ic" style="width:10px"><use href="#chev-r"/></svg></div><div>relbase</div><div></div><div>Active</div><div class="acts"><svg class="ic"><use href="#bolt"/></svg><svg class="ic"><use href="#edit"/></svg><svg class="ic"><use href="#copy"/></svg><svg class="ic"><use href="#trash"/></svg></div></div>
      <div class="row ds alt"><div class="exp"><svg class="ic" style="width:10px"><use href="#chev-r"/></svg></div><div>Skyledger - Sanbox</div><div>Skyledger.com</div><div>Active</div><div class="acts"><svg class="ic"><use href="#bolt"/></svg><svg class="ic"><use href="#edit"/></svg><svg class="ic"><use href="#copy"/></svg><svg class="ic"><use href="#trash"/></svg></div></div>
      <div class="row ds"><div class="exp"><svg class="ic" style="width:10px"><use href="#chev-r"/></svg></div><div>SLDG</div><div>Skyledger.com</div><div>Active</div><div class="acts"><svg class="ic"><use href="#bolt"/></svg><svg class="ic"><use href="#edit"/></svg><svg class="ic"><use href="#copy"/></svg><svg class="ic"><use href="#trash"/></svg></div></div>
      <div class="row ds alt"><div class="exp"><svg class="ic" style="width:12px"><use href="#chev-d"/></svg></div><div>sldg 44</div><div>Skyledger.com</div><div>Active</div><div class="acts"><svg class="ic"><use href="#bolt"/></svg><svg class="ic"><use href="#edit"/></svg><svg class="ic"><use href="#copy"/></svg><svg class="ic"><use href="#trash"/></svg></div></div>

      <div class="nest1">
        <div class="band sub">Data Objects <span class="add-btn">Add</span></div>
        <div class="row dobj col-head"><div></div><div>Data Object Name</div><div style="text-align:right;padding-right:8px">Actions</div></div>
        <div class="row dobj"><div class="exp"><svg class="ic" style="width:12px"><use href="#chev-d"/></svg></div><div style="padding-left:8px">Account</div><div class="count">28 fields</div><div class="del"><svg class="ic"><use href="#trash"/></svg></div></div>

        <div class="nest2">
          <div class="band sub">Fields <span class="add-btn">Add</span></div>
          <div class="row fld col-head"><div>Field Name</div><div>Data Type</div><div class="pk">Primary Key</div><div class="rules">Rule Types</div><div style="padding-left:20px">Actions</div></div>

          <div class="row fld"><div>Id</div><div>Common.ID</div><div class="pk"><span class="box on"><svg width="10" height="9" viewBox="0 0 10 9"><path d="M1 4.5l3 3 5-6" fill="none" stroke="#fff" stroke-width="1.8"/></svg></span></div><div class="rules"><svg class="ic"><use href="#r-text"/></svg><svg class="ic"><use href="#r-find"/></svg><svg class="ic" style="width:20px;height:20px"><use href="#r-dup"/></svg><svg class="ic"><use href="#r-branch"/></svg><svg class="ic"><use href="#r-globe"/></svg><svg class="ic"><use href="#r-list"/></svg></div><div class="acts"><svg class="ic"><use href="#edit"/></svg><svg class="ic"><use href="#trash"/></svg></div></div>
          <div class="row fld alt"><div>Name</div><div>Organization.Name</div><div class="pk"><span class="box"></span></div><div class="rules"><svg class="ic"><use href="#r-text"/></svg><svg class="ic"><use href="#r-find"/></svg><svg class="ic" style="width:20px;height:20px"><use href="#r-dup"/></svg><svg class="ic"><use href="#r-branch"/></svg><svg class="ic"><use href="#r-globe"/></svg><svg class="ic"><use href="#r-list"/></svg></div><div class="acts fade"><svg class="ic"><use href="#edit"/></svg><svg class="ic"><use href="#trash"/></svg></div></div>
          <div class="row fld"><div>Phone</div><div>Phone.Phone Number</div><div class="pk"><span class="box"></span></div><div class="rules"><svg class="ic"><use href="#r-text"/></svg><svg class="ic"><use href="#r-find"/></svg><svg class="ic" style="width:20px;height:20px"><use href="#r-dup"/></svg><svg class="ic"><use href="#r-branch"/></svg><svg class="ic"><use href="#r-globe"/></svg><svg class="ic"><use href="#r-list"/></svg></div><div class="acts fade"><svg class="ic"><use href="#edit"/></svg><svg class="ic"><use href="#trash"/></svg></div></div>
          <div class="row fld alt"><div>Type</div><div>Address.Address Line 1</div><div class="pk"><span class="box"></span></div><div class="rules"><svg class="ic"><use href="#r-text"/></svg><svg class="ic"><use href="#r-find"/></svg><svg class="ic" style="width:20px;height:20px"><use href="#r-dup"/></svg><svg class="ic"><use href="#r-branch"/></svg><svg class="ic"><use href="#r-globe"/></svg><svg class="ic"><use href="#r-list"/></svg></div><div class="acts fade"><svg class="ic"><use href="#edit"/></svg><svg class="ic"><use href="#trash"/></svg></div></div>
          <div class="row fld"><div>BillingCity</div><div>Address.City</div><div class="pk"><span class="box"></span></div><div class="rules"><svg class="ic"><use href="#r-text"/></svg><svg class="ic"><use href="#r-find"/></svg><svg class="ic" style="width:20px;height:20px"><use href="#r-dup"/></svg><svg class="ic"><use href="#r-branch"/></svg><svg class="ic"><use href="#r-globe"/></svg><svg class="ic"><use href="#r-list"/></svg></div><div class="acts"><svg class="ic"><use href="#edit"/></svg><svg class="ic"><use href="#trash"/></svg></div></div>
          <div class="row fld alt"><div>BillingCountry</div><div>Address.Country</div><div class="pk"><span class="box"></span></div><div class="rules"><svg class="ic"><use href="#r-text"/></svg><svg class="ic"><use href="#r-find"/></svg><svg class="ic" style="width:20px;height:20px"><use href="#r-dup"/></svg><svg class="ic"><use href="#r-branch"/></svg><svg class="ic"><use href="#r-globe"/></svg><svg class="ic"><use href="#r-list"/></svg></div><div class="acts fade"><svg class="ic"><use href="#edit"/></svg><svg class="ic"><use href="#trash"/></svg></div></div>
          <div class="row fld"><div>BillingLatitude</div><div>Geographic.Latitude</div><div class="pk"><span class="box"></span></div><div class="rules"><svg class="ic"><use href="#r-text"/></svg><svg class="ic"><use href="#r-find"/></svg><svg class="ic" style="width:20px;height:20px"><use href="#r-dup"/></svg><svg class="ic"><use href="#r-branch"/></svg><svg class="ic"><use href="#r-globe"/></svg><svg class="ic"><use href="#r-list"/></svg></div><div class="acts fade"><svg class="ic"><use href="#edit"/></svg><svg class="ic"><use href="#trash"/></svg></div></div>
          <div class="row fld alt"><div>BillingLongitude</div><div>Geographic.Longitude</div><div class="pk"><span class="box"></span></div><div class="rules"><svg class="ic"><use href="#r-text"/></svg><svg class="ic"><use href="#r-find"/></svg><svg class="ic" style="width:20px;height:20px"><use href="#r-dup"/></svg><svg class="ic"><use href="#r-branch"/></svg><svg class="ic"><use href="#r-globe"/></svg><svg class="ic"><use href="#r-list"/></svg></div><div class="acts fade"><svg class="ic"><use href="#edit"/></svg><svg class="ic"><use href="#trash"/></svg></div></div>
          <div class="row fld"><div>BillingState</div><div>Address.State or Province</div><div class="pk"><span class="box"></span></div><div class="rules off"><svg class="ic"><use href="#r-text"/></svg><svg class="ic"><use href="#r-find"/></svg><svg class="ic" style="width:20px;height:20px"><use href="#r-dup"/></svg><svg class="ic"><use href="#r-branch"/></svg><svg class="ic"><use href="#r-globe"/></svg><svg class="ic"><use href="#r-list"/></svg></div><div class="acts"><svg class="ic"><use href="#edit"/></svg><svg class="ic"><use href="#trash"/></svg></div></div>
          <div class="row fld alt"><div>BillingStreet</div><div>Address.Address Line 1</div><div class="pk"><span class="box"></span></div><div class="rules off"><svg class="ic"><use href="#r-text"/></svg><svg class="ic"><use href="#r-find"/></svg><svg class="ic" style="width:20px;height:20px"><use href="#r-dup"/></svg><svg class="ic"><use href="#r-branch"/></svg><svg class="ic"><use href="#r-globe"/></svg><svg class="ic"><use href="#r-list"/></svg></div><div class="acts"><svg class="ic"><use href="#edit"/></svg><svg class="ic"><use href="#trash"/></svg></div></div>
          <div class="row fld"><div>BillingPostalCode</div><div>Address.ZIP or Postal Code</div><div class="pk"><span class="box"></span></div><div class="rules off"><svg class="ic"><use href="#r-text"/></svg><svg class="ic"><use href="#r-find"/></svg><svg class="ic" style="width:20px;height:20px"><use href="#r-dup"/></svg><svg class="ic"><use href="#r-branch"/></svg><svg class="ic"><use href="#r-globe"/></svg><svg class="ic"><use href="#r-list"/></svg></div><div class="acts"><svg class="ic"><use href="#edit"/></svg><svg class="ic"><use href="#trash"/></svg></div></div>
          <div class="row fld alt"><div>LastModifiedDate</div><div>Common.Last Updated Date</div><div class="pk"><span class="box"></span></div><div class="rules off"><svg class="ic"><use href="#r-text"/></svg><svg class="ic"><use href="#r-find"/></svg><svg class="ic" style="width:20px;height:20px"><use href="#r-dup"/></svg><svg class="ic"><use href="#r-branch"/></svg><svg class="ic"><use href="#r-globe"/></svg><svg class="ic"><use href="#r-list"/></svg></div><div class="acts"><svg class="ic"><use href="#edit"/></svg><svg class="ic"><use href="#trash"/></svg></div></div>
          <div class="row fld"><div>Website</div><div>Organization.Website/URL</div><div class="pk"><span class="box"></span></div><div class="rules off"><svg class="ic"><use href="#r-text"/></svg><svg class="ic"><use href="#r-find"/></svg><svg class="ic" style="width:20px;height:20px"><use href="#r-dup"/></svg><svg class="ic"><use href="#r-branch"/></svg><svg class="ic"><use href="#r-globe"/></svg><svg class="ic"><use href="#r-list"/></svg></div><div class="acts"><svg class="ic"><use href="#edit"/></svg><svg class="ic"><use href="#trash"/></svg></div></div>
        </div>

        <div class="row dobj alt"><div class="exp"><svg class="ic" style="width:10px"><use href="#chev-r"/></svg></div><div style="padding-left:8px">Contact</div><div class="count">26 fields</div><div class="del"><svg class="ic"><use href="#trash"/></svg></div></div>
        <div class="row dobj"><div class="exp"><svg class="ic" style="width:10px"><use href="#chev-r"/></svg></div><div style="padding-left:8px">Lead</div><div class="count">17 fields</div><div class="del"><svg class="ic"><use href="#trash"/></svg></div></div>
      </div>

      <div class="row ds split"><div class="exp" style="justify-content:center"><svg class="ic" style="width:10px"><use href="#chev-r"/></svg></div><div>sldg 99</div><div>Skyledger.com</div><div>Active</div><div class="acts" style="justify-content:flex-end"><svg class="ic"><use href="#bolt"/></svg><svg class="ic"><use href="#edit"/></svg><svg class="ic"><use href="#copy"/></svg><svg class="ic"><use href="#trash"/></svg></div></div>
      <div class="row ds split alt"><div class="exp" style="justify-content:center"><svg class="ic" style="width:10px"><use href="#chev-r"/></svg></div><div>SLDG - Field Entry Test</div><div>Skyledger.com</div><div>Active</div><div class="acts" style="justify-content:flex-end"><svg class="ic"><use href="#bolt"/></svg><svg class="ic"><use href="#edit"/></svg><svg class="ic"><use href="#copy"/></svg><svg class="ic"><use href="#trash"/></svg></div></div>

      <div class="pager">6 of 6 records
        <select><option>20</option></select>
        <div class="pages">
          <svg width="14" height="10" viewBox="0 0 14 10"><path d="M7 0 1 5l6 5zM13 0 7 5l6 5z" fill="#c3c6d6"/></svg>
          <svg width="8" height="10" viewBox="0 0 8 10"><path d="M7 0 1 5l6 5z" fill="#c3c6d6"/></svg>
          <span>1</span>
          <svg width="8" height="10" viewBox="0 0 8 10"><path d="M1 0l6 5-6 5z" fill="#1f2d86"/></svg>
          <svg width="14" height="10" viewBox="0 0 14 10"><path d="M1 0l6 5-6 5zM7 0l6 5-6 5z" fill="#1f2d86"/></svg>
        </div>
      </div>
    </section>
  </main>

  <footer class="footer">Acma Data 2018. All rights reserved.</footer>
</div>
</body>
</html>
```